Chinese citizens moving to SYDNEY!

We need an A5 size flier for our new business. We would like this to be a fold-out flyer (brochure-style, i.e. 4 sides - front cover, middle, back cover). Full colour print (or 4 colour if it can be done without compromising the look). We need two versions of the same flyer - one in Chinese and one in English. Same design and imagery, just different languages. Copy is attached with imagery (subject to change once we source high res images).

Target Market(s)

Chinese citizens looking to emigrate to Sydney AND Chinese citizens who have recently moved to Sydney.

Industry/Entity Type

Business

Font styles to use
Sans Serif

Colors
ec1f27
000000
ffffff
fece3e

Requirements
Must have
• The front cover of the flier must be clean looking and show just our business name and tag line, along with an image of Sydney Harbour (provided). Main information ideally to be spread across the 2 centre pages with the back page quite clean, but if the text is too small we could consider it being spread across the remaining 3 pages (i.e. centre of the brochure, then the back cover).
• We would like it to be a clean and easy to read design. Suggested colours are written in the brief.
• It would be ideal to have a designer who can read Mandarin so that they know which characters make up a headline, which characters should not be spaced over two rows of text etc.

```html
<!DOCTYPE html>
<html lang="en">
<head>
<meta charset="utf-8">
<title>Harbourline Concierge – Relocation Flyer</title>
<link rel="stylesheet" href="https://fonts.googleapis.com/css2?family=Arimo:wght@400;700&family=Open+Sans:wght@600;700&display=swap">
<style>
  :root {
    --red: #ec1f27;
    --red-deep: #d0141c;
    --red-text: #b8121a;
    --yellow: #fece3e;
    --gold: #fbc531;
    --orange: #f7a740;
    --cream: #fde9bf;
    --cream-light: #fef3d6;
    --green: #5aa63a;
    --tab-orange: #f9b54a;
    --ink: #1a1a1a;
    --white: #ffffff;
    --violet: #4b3a8f;
    --pink: #e6168a;
  }
  * { box-sizing: border-box; margin: 0; padding: 0; }
  html, body { width: 1200px; height: 1200px; overflow: hidden; background: var(--white); }
  body { font-family: "Arimo", Arial, sans-serif; color: var(--ink); }

  .flyer { position: absolute; left: 198px; top: 32px; width: 804px; height: 1136px; overflow: hidden; background: var(--cream-light); }
  .backdrop { position: absolute; inset: 0; }
  .abs { position: absolute; }

  .brand { left: 0; top: 17px; width: 272px; text-align: center; }
  .brand-name { font-family: "Open Sans", Arial, sans-serif; font-weight: 700; font-size: 19px; line-height: 24px; color: var(--yellow); white-space: nowrap; }
  .brand-tagline { font-family: "Open Sans", Arial, sans-serif; font-weight: 700; font-size: 10.5px; color: var(--white); margin-top: 5px; white-space: nowrap; }

  .framed { border: 5px solid var(--white); box-shadow: 0 1px 3px rgba(0,0,0,.25); }

  .label { font-family: "Open Sans", Arial, sans-serif; font-weight: 700; color: var(--violet); font-size: 10px; white-space: nowrap; }
  .about-label { left: 362px; top: 114px; width: 80px; text-align: center; }
  .services-label { left: 510px; top: 31px; width: 280px; text-align: center; }

  .about { left: 285px; top: 180px; width: 234px; font-size: 11.2px; line-height: 11.8px; }
  .about p + p { margin-top: 11.8px; }

  .tab { height: 18px; width: 168px; border-radius: 4px; font-family: "Open Sans", Arial, sans-serif; font-weight: 700; font-size: 10px; line-height: 18px; padding-left: 6px; box-shadow: 2px 2px 0 rgba(230,110,40,.7); white-space: nowrap; }
  .tab-school { left: 542px; top: 72px; background: var(--tab-orange); color: #6b5a4a; }
  .tab-green { background: var(--green); color: var(--white); top: 589px; }

  .list { list-style: none; font-size: 11.2px; line-height: 12.8px; }
  .list li { position: relative; }
  .list-school { left: 549px; top: 106px; width: 254px; color: var(--red-text); }
  .list-school li { padding-left: 15px; }
  .list-school li::before { content: ""; position: absolute; left: 0; top: 2px; width: 9px; height: 9px; border-radius: 50%; background: var(--gold); box-shadow: inset 0 0 0 1.5px #9a6a10; }

  .col { top: 623px; }
  .col li { padding-left: 19px; }
  .tick { position: absolute; left: 0; top: 1px; width: 11px; height: 11px; }
</style>
</head>
<body>
<main class="flyer">

  <svg class="backdrop" width="804" height="1136" viewBox="0 0 804 1136" aria-hidden="true">
    <rect x="0" y="0" width="804" height="568" fill="var(--cream)"/>
    <path d="M0 0 H804 V190 C700 180 600 140 480 130 C330 118 150 120 0 120 Z" fill="var(--red)"/>
    <path d="M0 120 C150 112 330 110 480 122 C600 132 700 170 804 182 V220 C700 208 600 165 470 150 C330 136 150 140 0 148 Z" fill="var(--yellow)"/>
    <path d="M268 150 C400 150 560 175 804 222 V380 C640 410 460 360 268 330 Z" fill="var(--orange)" opacity=".85"/>
    <path d="M250 420 C420 470 600 450 804 420 V552 H250 Z" fill="var(--gold)"/>
    <path d="M250 450 C420 500 600 480 804 450 V470 C600 500 420 520 250 475 Z" fill="var(--cream-light)" opacity=".7"/>
    <rect x="0" y="552" width="804" height="16" fill="var(--red)"/>
    <rect x="0" y="568" width="804" height="568" fill="var(--cream-light)"/>
    <path d="M40 568 L190 568 L90 900 Z" fill="var(--cream)"/>
    <path d="M260 568 L360 568 L300 760 Z" fill="#fff6c0"/>
    <path d="M420 568 L540 568 L470 800 Z" fill="#fff6c0"/>
    <path d="M600 568 L700 568 L660 740 Z" fill="var(--cream)"/>
    <path d="M290 640 L480 900 L290 900 Z" fill="#fde2a6" opacity=".7"/>
    <path d="M560 700 L804 620 L804 820 Z" fill="#fbd7a8" opacity=".7"/>
    <path d="M268 920 C420 880 560 830 804 800 V1136 H268 Z" fill="var(--red)"/>
    <path d="M268 935 C420 895 560 850 804 820 V860 C560 880 430 920 268 960 Z" fill="var(--gold)"/>
    <path d="M0 1040 C150 1060 400 1070 804 1060 V1136 H0 Z" fill="var(--red)"/>
    <path d="M0 1052 C150 1070 400 1078 804 1068 V1076 C400 1086 150 1080 0 1062 Z" fill="var(--pink)"/>
    <path d="M0 1090 C160 1104 420 1110 804 1100 V1136 H0 Z" fill="var(--red-deep)"/>
  </svg>

  <header class="abs brand">
    <div class="brand-name">HARBOURLINE CONCIERGE</div>
    <div class="brand-tagline">Sydney’s Relocation and Settlement Experts</div>
  </header>

  <div class="abs" role="img" aria-label="Dark silhouette of the Sydney skyline with its red reflection" style="left:278px;top:8px;width:244px;height:108px;background:linear-gradient(180deg,#3a3a3a 0%,#3a3a3a 48%,#b81219 52%,#e0262d 100%);opacity:.9;"></div>

  <div class="abs" role="img" aria-label="Photo of Sydney Harbour Bridge and city skyline under a blue sky" style="left:0;top:124px;width:268px;height:172px;background:linear-gradient(180deg,#4a8fd6 0%,#8fc2ec 55%,#3a6a8c 75%,#2a4f6a 100%);"></div>

  <div class="abs" role="img" aria-label="Illustration of red service icons for school, home, cycling, shopping and care" style="left:10px;top:322px;width:270px;height:226px;border-radius:110px;background:radial-gradient(circle at 55% 45%,#ec1f27 0%,#ef4a3a 55%,rgba(253,233,191,0) 80%);"></div>

  <h2 class="abs label about-label">About Us:</h2>
  <section class="abs about">
    <p>Harbourline Concierge is a premium lifestyle service supporting families who are planning or currently migrating to and investing in Australia.</p>
    <p>Specialising in the city of Sydney, Harbourline Concierge helps families to feel comfortable and at home as soon as possible.</p>
    <p>Our team of local experts provide support every step of the way – answering questions, providing advice and breaking down the language barrier.</p>
    <p>Our services are highly customisable to suit the needs of individual families. Whether it’s finding the best school for your children, the help you need in your home, knowing where to buy your favourite groceries or an introduction to a great GP or Specialist – Harbourline Concierge will cater to your every need.</p>
    <p>Your family will be assigned a professional Personal Assistant who is fluent in both English and Mandarin, making the process of migrating less daunting and more enjoyable.</p>
  </section>

  <h2 class="abs label services-label">Our services include but are not limited to:</h2>
  <h3 class="abs tab tab-school">1. School</h3>
  <ul class="abs list list-school">
    <li>Recommend the best schools and childcare centres</li>
    <li>Compare school rankings and academic results</li>
    <li>Arrange private tours of schools and meetings with Principals</li>
    <li>Manage the school application process through to completion</li>
    <li>Assist with starting school, such as purchase of uniforms and textbooks, understanding school procedures and more</li>
    <li>Appoint private tutors to assist with learning English and completing homework assignments</li>
    <li>Organise extra curricular activities, such as piano lessons, tennis lessons and more</li>
    <li>Translate all school correspondence such as academic report cards, homework assignments and more</li>
  </ul>

  <div class="abs framed" role="img" aria-label="Photo of schoolgirls in uniform walking by the harbour carrying folders" style="left:538px;top:362px;width:258px;height:178px;background:linear-gradient(180deg,#2e3540 0%,#6d7f8c 45%,#c9d3d8 60%,#3d4550 100%);"></div>

  <h3 class="abs tab tab-green" style="left:16px">2. Home and Car</h3>
  <h3 class="abs tab tab-green" style="left:285px">3. Everyday Necessities</h3>
  <h3 class="abs tab tab-green" style="left:551px">4. Health and Lifestyle</h3>

  <svg width="0" height="0" style="position:absolute">
    <symbol id="tick" viewBox="0 0 12 12"><path d="M1 6.5 L4.5 10 L11 1.5" stroke="var(--green)" stroke-width="2.6" fill="none" stroke-linecap="round" stroke-linejoin="round"/></symbol>
  </svg>

  <ul class="abs list col" style="left:16px;width:230px">
    <li><svg class="tick"><use href="#tick"/></svg>Recommend the best suburbs for families</li>
    <li><svg class="tick"><use href="#tick"/></svg>Make introductions to Real Estate Agents and support the buying process</li>
    <li><svg class="tick"><use href="#tick"/></svg>Arrange unpacking and home organisation services</li>
    <li><svg class="tick"><use href="#tick"/></svg>Assist to purchase furniture and appliances</li>
    <li><svg class="tick"><use href="#tick"/></svg>Source the best utility companies and organise connection – electricity, gas, water, phone, internet, TV and more</li>
    <li><svg class="tick"><use href="#tick"/></svg>Appoint staff for your home such as cleaners, gardeners and more</li>
    <li><svg class="tick"><use href="#tick"/></svg>Compare home insurance options and assist with purchasing</li>
    <li><svg class="tick"><use href="#tick"/></svg>Assist with car purchasing, leasing and acquiring necessary insurance</li>
  </ul>

  <ul class="abs list col" style="left:286px;width:240px">
    <li><svg class="tick"><use href="#tick"/></svg>Explain local grocery options such as supermarkets, specialty stores, Asian grocers and more</li>
    <li><svg class="tick"><use href="#tick"/></svg>Recommend beauty and wellness services such as hair salons, nail parlours, beauty salons and more</li>
    <li><svg class="tick"><use href="#tick"/></svg>Explain retail shopping options such major shopping centres and luxury brands</li>
    <li><svg class="tick"><use href="#tick"/></svg>Source quality trades people such as plumbers, electricians, painters and more</li>
    <li><svg class="tick"><use href="#tick"/></svg>Assist with government registrations such as drivers license, Medicare and more</li>
    <li><svg class="tick"><use href="#tick"/></svg>Assist to open bank accounts and set up online banking</li>
    <li><svg class="tick"><use href="#tick"/></svg>Assist to set up memberships – library, gym, golf club and more</li>
    <li><svg class="tick"><use href="#tick"/></svg>Explain private and public transport options</li>
    <li><svg class="tick"><use href="#tick"/></svg>Organise private and group language classes</li>
    <li><svg class="tick"><use href="#tick"/></svg>Translate documents and mail</li>
  </ul>

  <ul class="abs list col" style="left:552px;width:226px">
    <li><svg class="tick"><use href="#tick"/></svg>Compare health insurance options</li>
    <li><svg class="tick"><use href="#tick"/></svg>Recommend the best medical professionals – GP, Dentist, Acupuncture and more</li>
    <li><svg class="tick"><use href="#tick"/></svg>Recommend restaurants</li>
    <li><svg class="tick"><use href="#tick"/></svg>Suggest the best local parks to visit and other outdoor activities</li>
    <li><svg class="tick"><use href="#tick"/></svg>Explain local dangers such as Australian wildlife, beach safety and more</li>
    <li><svg class="tick"><use href="#tick"/></svg>Suggest family outings, recommend holiday destinations, plan children’s birthday parties, play dates and more</li>
    <li><svg class="tick"><use href="#tick"/></svg>Arrange Private chauffers</li>
  </ul>

  <div class="abs framed" role="img" aria-label="Photo of a modern two-storey family home at dusk with a car in the driveway" style="left:6px;top:866px;width:258px;height:176px;background:linear-gradient(180deg,#2b3a66 0%,#5c6a8a 40%,#c9c2b0 60%,#4a4f3a 100%);"></div>
  <div class="abs framed" role="img" aria-label="Photo of a supermarket fresh produce section with fruit displays" style="left:274px;top:924px;width:258px;height:176px;background:linear-gradient(180deg,#3a3028 0%,#7a6a58 35%,#c94a2a 60%,#e8c43a 85%,#8ab43a 100%);"></div>
  <div class="abs framed" role="img" aria-label="Photo of a bright restaurant interior with wooden tables and chairs" style="left:536px;top:810px;width:220px;height:144px;background:linear-gradient(180deg,#6a4a2e 0%,#b9d3e0 35%,#8a5a34 65%,#5a3a22 100%);"></div>
  <div class="abs framed" role="img" aria-label="Photo of a family relaxing on a picnic blanket in a sunny park" style="left:572px;top:948px;width:223px;height:152px;background:linear-gradient(180deg,#d8e6a0 0%,#9ac25a 45%,#5f8f2e 100%);"></div>

</main>
</body>
</html>
```